Wild Mo's Wine Label Project

We need a new entry level wine label called "Wild Mo's" for a range of wines we are developing from inland Australia. Our company is made up of three youngish guys who live hard and love taking the mickey. Wild Mo is Wild Moss - the largest and loudest of the three partners (and ideally this label will take the mickey out of him). We've grown the grapes ourselves for this first release which will be a 2012 Pinot Gris. Wine style is dry, young, fresh and contemporary and pitched at the sub AUD $10 retail price point. The package will be flint (clear) claret shape bottle with plain screwcap (colour matched to suit the winning label design).

I've attached a couple of photos of Wild Moss to give you some idea of his presence and persona.

Target Market(s)

Semi educated 25 - 40 year old wine drinkers. Skewed towards females.

Industry/Entity Type

Retail

Requirements
Should not have
• Anything traditional or old fashioned

```html
<!DOCTYPE html>
<html lang="en">
<head>
<meta charset="utf-8">
<title>Wild Moss Pinot Gris 2012 – Label</title>
<link rel="stylesheet" href="https://fonts.googleapis.com/css2?family=Arimo:wght@400;700&display=swap">
<style>
  :root {
    --page-bg: #ffffff;
    --label-navy: #1d2a6e;
    --label-olive: #9c9a3f;
    --text-white: #ffffff;
  }
  html, body {
    margin: 0;
    padding: 0;
    width: 799px;
    height: 1200px;
    overflow: hidden;
    background: var(--page-bg);
  }
  .canvas {
    position: relative;
    width: 799px;
    height: 1200px;
  }
  .wine-label {
    position: absolute;
    left: 40px;
    top: 404px;
    width: 720px;
    height: 392px;
    background: var(--label-navy);
    overflow: hidden;
  }
  .label-swoosh {
    position: absolute;
    inset: 0;
    width: 100%;
    height: 100%;
  }
  .label-swoosh .olive-band { fill: var(--label-olive); }
  .brand-name,
  .varietal,
  .style-note,
  .origin {
    position: absolute;
    margin: 0;
    white-space: nowrap;
    line-height: 1;
    font-family: "Arimo", sans-serif;
  }
  .brand-name {
    left: 164px;
    top: 38px;
    font-size: 62px;
    font-weight: 400;
    letter-spacing: 3px;
    color: var(--text-white);
  }
  .varietal {
    left: 180px;
    top: 150px;
    font-size: 48px;
    font-weight: 400;
    color: var(--text-white);
  }
  .varietal .vintage { color: var(--label-olive); }
  .style-note {
    left: 287px;
    top: 240px;
    font-size: 42px;
    font-weight: 400;
    color: var(--label-olive);
  }
  .origin {
    left: 299px;
    top: 356px;
    font-size: 19px;
    font-weight: 700;
    color: var(--text-white);
  }
</style>
</head>
<body>
  <main class="canvas">
    <section class="wine-label">
      <svg class="label-swoosh" viewBox="0 0 720 392" preserveAspectRatio="none" aria-hidden="true">
        <path class="olive-band" d="M0,300 C250,336 500,300 720,150 L720,392 L0,392 Z"/>
      </svg>
      <h1 class="brand-name">Wild Moss</h1>
      <p class="varietal">Pinot Gris <span class="vintage">2012</span></p>
      <p class="style-note">young</p>
      <p class="origin">Australia</p>
    </section>
  </main>
</body>
</html>
```